Cradlecraft by Lorna Business Card Design

i am starting a new business as a reborn artist (that is painting dolls to make them look like real live babies)

i eventually want to sell the dolls that i make and have classed in reborning. but at the moment i just want to get my name out there.

I do not currently have images of the dolls so cannot have an image in the design.

Non compulsory thoughts: i like the look of old wood, white and baby pink,even hot pink, and lace, denim. i had in mind something like a tiny baby in a old cradle or something, a old drawer, box, something different or unusual, it has to be a girl baby. i am also open to other thoughts on the matter. i would like plain writing not all swirly
Updates

Sorry to change but would like it to read country cradlecraft by lorna.

Industry/Entity Type

Painting

Contact Information for Business Card

Cradlecraft by Lorna
cradle dolls that never grow up
Reborn Artist Lorna Whitby
0431 756 842
marlo.t@quillbox.com

```html
<!DOCTYPE html>
<html lang="en">
<head>
<meta charset="utf-8">
<title>Cradlecraft – Business Card</title>
<link rel="stylesheet" href="https://fonts.googleapis.com/css2?family=Open+Sans:wght@400;600;700&family=Questrial&display=swap">
<style>
  :root {
    --page-bg: #e8e4e4;
    --card-pink: #f7dce9;
    --lace-light: #fbeaf2;
    --hot-pink: #c8136e;
    --wood-brown: #5b3518;
    --wood-dark: #3f230e;
    --text-brown: #4a2a12;
    --band-text: #f6e7ee;
  }
  * { margin: 0; padding: 0; box-sizing: border-box; }
  html, body {
    width: 1200px;
    height: 800px;
    overflow: hidden;
    background: var(--page-bg);
  }
  .canvas {
    position: relative;
    width: 1200px;
    height: 800px;
  }
  .card {
    position: absolute;
    left: 100px;
    top: 115px;
    width: 1000px;
    height: 570px;
    background: radial-gradient(ellipse at 60% 40%, var(--lace-light), var(--card-pink) 75%);
    box-shadow: 0 6px 22px rgba(0,0,0,0.18);
    overflow: hidden;
  }
  .cradle-photo {
    position: absolute;
    left: 70px;
    top: 70px;
    width: 290px;
    height: 190px;
    border-radius: 4px;
    background: linear-gradient(160deg, #f3e4e8 0%, #c99a7a 45%, #6b3b1c 100%);
  }
  .brand {
    position: absolute;
    right: 90px;
    top: 90px;
    font-family: "Open Sans", sans-serif;
    font-weight: 400;
    font-size: 64px;
    line-height: 1.1;
    color: var(--text-brown);
    white-space: nowrap;
  }
  .tagline-band {
    position: absolute;
    left: 0;
    top: 262px;
    width: 100%;
    height: 36px;
    background: linear-gradient(180deg, var(--wood-brown), var(--wood-dark));
    display: flex;
    align-items: center;
    justify-content: center;
  }
  .tagline {
    font-family: "Questrial", sans-serif;
    font-size: 20px;
    letter-spacing: 9px;
    color: var(--band-text);
    white-space: nowrap;
  }
  .contact {
    position: absolute;
    left: 400px;
    top: 322px;
    width: 360px;
    text-align: center;
    font-family: "Open Sans", sans-serif;
    color: var(--text-brown);
  }
  .contact-name {
    font-size: 30px;
    font-weight: 700;
    color: var(--hot-pink);
    line-height: 1.15;
  }
  .contact-role {
    font-size: 20px;
    font-weight: 400;
    line-height: 1.3;
    margin-bottom: 26px;
  }
  .contact-phone,
  .contact-email {
    font-size: 28px;
    font-weight: 600;
    line-height: 1.25;
  }
</style>
</head>
<body>
  <main class="canvas">
    <section class="card">
      <div class="cradle-photo" role="img" aria-label="Photo of a doll in an old wooden rocking cradle"></div>

      <p class="brand">Cradlecraft</p>

      <div class="tagline-band">
        <p class="tagline">cradle dolls that never grow up</p>
      </div>

      <div class="contact">
        <p class="contact-name">Lorna Whitby</p>
        <p class="contact-role">Reborn Artist</p>
        <p class="contact-phone">0431 756 842</p>
        <p class="contact-email">marlo.t@quillbox.com</p>
      </div>
    </section>
  </main>
</body>
</html>
```